*** Bakery Needs a Business Card

I need a business card for my new bakery - Pine Lane Baking Dept. We make biscuits, cakes, muffins and other sweets. Our food is honest, wholesome and down to earth - i'd love this to be reflected in the design of the card. The design MUST include our logo (see the attached image - which needs to be replicated). The design should only use 2 or at most 3 colours.

Industry/Entity Type

Bakery

Requirements
Must have
• Must include my logo.
Must have a clean, simple design.
Space for my name, my title, my phone number, my facebook page (I will provide details later)
Should not have
• Must not have lots of bright colours.
Must not have any unnescassry graphics.

```html
<!DOCTYPE html>
<html lang="en">
<head>
<meta charset="utf-8">
<title>Pine Lane Baking Dept. – Business Card</title>
<link rel="stylesheet" href="https://fonts.googleapis.com/css2?family=Josefin+Sans:wght@300;400&display=swap">
<style>
  :root {
    --kraft: #c7a458;
    --kraft-light: #ddc48a;
    --kraft-dark: #b08c42;
    --ink-red: #8e1b10;
  }
  * { margin: 0; padding: 0; box-sizing: border-box; }
  html, body {
    width: 1200px;
    height: 741px;
    overflow: hidden;
    background: var(--kraft);
  }
  .card {
    position: relative;
    width: 1200px;
    height: 741px;
    overflow: hidden;
    background:
      radial-gradient(ellipse at 92% 4%, var(--kraft-light) 0%, rgba(221,196,138,0) 45%),
      radial-gradient(ellipse at 10% 95%, var(--kraft-dark) 0%, rgba(176,140,66,0) 55%),
      var(--kraft);
    font-family: "Josefin Sans", "Century Gothic", sans-serif;
    color: var(--ink-red);
  }
  .brand-name {
    position: absolute;
    left: 168px;
    top: 150px;
    font-size: 150px;
    font-weight: 400;
    line-height: 1;
    letter-spacing: 2px;
    text-transform: uppercase;
    white-space: nowrap;
  }
  .contact {
    position: absolute;
    left: 284px;
    top: 432px;
    line-height: 1;
  }
  .contact__name {
    font-size: 52px;
    font-weight: 400;
    margin-bottom: 14px;
  }
  .contact__title {
    font-size: 34px;
    font-weight: 300;
    margin-bottom: 16px;
  }
  .contact__phone {
    font-size: 42px;
    font-weight: 300;
    margin-bottom: 14px;
  }
  .contact__web {
    font-size: 26px;
    font-weight: 300;
  }
</style>
</head>
<body>
  <main class="card">
    <div class="brand-name">Pine Lane</div>
    <section class="contact">
      <p class="contact__name">name goes here</p>
      <p class="contact__title">title goes here</p>
      <p class="contact__phone">ph: 123123123</p>
      <p class="contact__web">www.pinelanebaking.com/page</p>
    </section>
  </main>
</body>
</html>
```